Bottlecap Decals Inc. NEED DESIGNS FOR THE HOLIDAY STICKERS

We need 6 designs for the HOLIDAY SET of Bottlecap Decals. I have attached some imagery that we like as well as the flagship pack of stickers that were also designed by you AWESOME DESIGNERS!! You are not limited to this imagery, it is only to show you what style we like but remember, YOU ARE THE ARTIST! Each design needs to have a "TO: & FROM:" for people to write in their name and the recipients name. We need designs for the following occasions:

1. HALLOWEEN
2. HAPPY HOLIDAYS (THANKSGIVING, CHRISTMAS, WINTER, LEAVES)
3. ST. PATRICK'S DAY
4. "LET'S CELEBRATE" PATRIOTIC THEME (JULY 4TH, VETERANS DAY, MEMORIAL DAY COMBINED)
5. HAPPY NEW YEAR
6. SUMMER THEME GENERIC

***these 6 designs must fit on one of die cut shapes which are included in the brief***

**PLEASE SUBMIT YOUR IDEA FOR AS MANY DESIGNS AS YOU CAN (PREFERABLY ALL 6). WE NEED 6 DESIGNS SO IF 4 OF YOURS ARE GOOD AND 2 OF ANOTHERS ARE GOOD, YOU WOULD WIN 1ST AND THEY WOULD WIN 2ND.

Font styles to use
Serif
Sans Serif
Decorative
Script

Requirements
Must have
• - lines for "to" and "from"
• - must fit on a die cut shape (provided)
• - must be FUN and colorful!!
Nice to have
• color, imagery, fun!

```html
<!DOCTYPE html>
<html lang="en">
<head>
<meta charset="utf-8">
<title>Let's Celebrate – Holiday Sticker</title>
<link rel="stylesheet" href="https://fonts.googleapis.com/css2?family=Great+Vibes&family=Oswald:wght@600&family=Open+Sans:wght@400&display=swap">
<style>
  :root {
    --flag-red: #d42027;
    --flag-blue: #0f6482;
    --outline-teal: #1d4f5f;
    --paper: #ffffff;
    --stage: #eeeeee;
    --stage-edge: #d9d9d9;
  }
  * { margin: 0; padding: 0; box-sizing: border-box; }
  html, body {
    width: 1200px;
    height: 900px;
    overflow: hidden;
  }
  body {
    background: radial-gradient(ellipse at center, var(--stage) 55%, var(--stage-edge) 100%);
    position: relative;
  }
  .sticker {
    position: absolute;
    left: 300px;
    top: 80px;
    width: 600px;
    height: 720px;
    filter: drop-shadow(0 6px 10px rgba(0,0,0,0.12));
  }
  .sticker svg { display: block; width: 100%; height: 100%; }
  .greeting-script {
    font-family: "Great Vibes", cursive;
    font-size: 56px;
    fill: var(--paper);
  }
  .greeting-headline {
    font-family: "Oswald", sans-serif;
    font-weight: 600;
    font-size: 78px;
    letter-spacing: 1px;
    fill: var(--paper);
  }
  .field-label {
    font-family: "Open Sans", sans-serif;
    font-size: 15px;
    fill: #222222;
  }
  .field-line {
    stroke: #333333;
    stroke-width: 1;
    stroke-dasharray: 1.5 2;
  }
</style>
</head>
<body>
  <div class="sticker">
    <svg viewBox="0 0 600 720" xmlns="http://www.w3.org/2000/svg">
      <defs>
        <clipPath id="die-cut">
          <path d="M0,125 A40,40 0 0 0 40,95 Q300,-20 560,95 A40,40 0 0 0 600,125 L600,640 A40,40 0 0 0 560,680 L560,720 L40,720 L40,680 A40,40 0 0 0 0,640 Z"/>
        </clipPath>
        <radialGradient id="burst-tone" cx="50%" cy="100%" r="90%">
          <stop offset="0%" stop-color="#f6d3d4"/>
          <stop offset="55%" stop-color="#e6686d"/>
          <stop offset="100%" stop-color="#d42027"/>
        </radialGradient>
        <linearGradient id="lower-burst-tone" x1="0" x2="1" y1="0" y2="0">
          <stop offset="0%" stop-color="#d42027"/>
          <stop offset="22%" stop-color="#ec9a9d"/>
          <stop offset="35%" stop-color="#ffffff"/>
          <stop offset="65%" stop-color="#ffffff"/>
          <stop offset="78%" stop-color="#ec9a9d"/>
          <stop offset="100%" stop-color="#d42027"/>
        </linearGradient>
        <linearGradient id="panel-shade" x1="0" x2="0" y1="0" y2="1">
          <stop offset="0%" stop-color="#0b5570"/>
          <stop offset="12%" stop-color="#0f6482"/>
          <stop offset="88%" stop-color="#0f6482"/>
          <stop offset="100%" stop-color="#0b5570"/>
        </linearGradient>
      </defs>

      <g clip-path="url(#die-cut)">
        <rect class="sticker-paper" x="0" y="0" width="600" height="720" fill="var(--paper)"/>

        <rect class="sunburst-top" x="0" y="0" width="600" height="190" fill="url(#burst-tone)" role="img" aria-label="Red and white sunburst rays fanning out behind a star emblem"/>

        <g class="top-stripe-band">
          <rect x="0" y="187" width="600" height="4" fill="var(--flag-red)"/>
          <rect class="star-row" x="0" y="200" width="600" height="32" fill="var(--flag-blue)" role="img" aria-label="Blue band with a row of white stars"/>
          <rect x="0" y="241" width="600" height="5" fill="var(--flag-red)"/>
        </g>

        <rect class="title-panel" x="0" y="258" width="600" height="228" fill="url(#panel-shade)"/>

        <g class="bottom-stripe-band">
          <rect x="0" y="487" width="600" height="5" fill="var(--flag-red)"/>
          <rect class="star-row" x="0" y="505" width="600" height="34" fill="var(--flag-blue)" role="img" aria-label="Blue band with a row of white stars"/>
          <rect x="0" y="546" width="600" height="4" fill="var(--flag-red)"/>
        </g>

        <rect class="sunburst-bottom" x="0" y="560" width="600" height="160" fill="url(#lower-burst-tone)" role="img" aria-label="Red and white sunburst rays along the lower corners"/>
        <path class="name-field-area" d="M185,560 L415,560 L440,720 L160,720 Z" fill="var(--paper)"/>
      </g>

      <path class="die-cut-inner-line" d="M10,132 A42,42 0 0 0 45,104 Q300,-5 555,104 A42,42 0 0 0 590,132 L590,634 A42,42 0 0 0 552,672 L552,708 L48,708 L48,672 A42,42 0 0 0 10,634 Z" fill="none" stroke="var(--outline-teal)" stroke-width="2.5"/>

      <rect class="crest-emblem" x="250" y="46" width="96" height="96" rx="16" fill="var(--flag-blue)" role="img" aria-label="Layered red, white and blue star emblem"/>

      <rect class="headline-star-arc" x="80" y="296" width="440" height="70" fill="#0f6482" role="img" aria-label="Arc of white stars around the greeting"/>

      <text class="greeting-script" x="300" y="336" text-anchor="middle">Let's</text>
      <text class="greeting-headline" x="300" y="432" text-anchor="middle">CELEBRATE</text>

      <g class="recipient-fields">
        <text class="field-label" x="218" y="627" text-anchor="end">TO</text>
        <line class="field-line" x1="222" y1="628" x2="420" y2="628"/>
        <text class="field-label" x="218" y="668" text-anchor="end">FROM</text>
        <line class="field-line" x1="222" y1="669" x2="420" y2="669"/>
      </g>
    </svg>
  </div>
</body>
</html>
```